Home page design for Drone video business (the Business focusses on home videos for realtors)

Dear reader,

*I NEED DESIGNS OF ALL THE PAGES*
We need a first design of a homepage and of 4 other pages of the website of a business that sells drone video services. All the pages will need to be in the similar design style.
The video's are targeted at consumers that want to sell there home and would like to have a cool drone video of photos of their home.

How does the website look:
- has a navbar on top
- A cool looking banner of an areal drone.
- A Big header: with company name: SkyNestClips
- A smaller subheader: We film your home to increase your chances of sale
- Then a section with a Big header: How does it work
- In this section a place for a vimeo explainitory video
- Then a similar navbar styled bar with a phone number and a email address
- Then a section where the videos porfolio is displayed in a cool way
- Inside this sectiona header: Our work

- A section with header: Why us?
- 4 symbols here with a subheader and some lorum ipsum text underneath (see wireframe images)

- Under that a: Contact us
- where you can put in name, email, phone, message box and a send button

- At the bottom a footer with phone number and a fake address for now.

Be creative. Use creative but serious color.
Use a serious font. Make it a sharp design. Sharp lines. Not to dark design and not to light design.

The wireframes are the same kind of images.
PLEASE PUT IN DESIGNS OF ALL THE PAGES

Good luck

Target Market(s)

People that want to sell home and want to make a cool drone video or photos of their home.

Industry/Entity Type

Business

Contact Information for Business Card

Lucas Verbeek
lucas@skynestclips.example
+31647203519

Logo Text

SkyNestClips

Number of Pages Required

1 page

Font styles to use
Sans Serif

Requirements
Must have
• All the sections as explained in the instructions.
• The nav bar should have an about us, services, portfolio and a contact us buttons.
• See instruction for details.
• Must include designs of the front page, contact us, our services, portfolio and contact us.
• If you do add some designs for the "about us", "services", "prices", "portfolio" and "contact us" pages, you make a way better chance of winning the competition.
Nice to have
• designs for the other pages as described at the Must haves. You make a better chance of winning if you include them. Look at the wireframes to see the mockups for those pages. think creative about what kind of sections and design should be included in those pages.
Should not have
• bad designs.

```html
<!DOCTYPE html>
<html lang="en">
<head>
<meta charset="utf-8">
<title>SkyNestClips – Home</title>
<link href="https://fonts.googleapis.com/css2?family=Arimo:wght@400;700&display=swap" rel="stylesheet">
<style>
:root{
  --green:#8cc43f;
  --green-dark:#6fa52b;
  --ink:#2b2b2b;
  --muted:#777;
  --light:#f3f4f6;
  --dark:#2e2e2e;
  --darker:#1c1c1c;
  --white:#fff;
  --player:#141414;
}
*{margin:0;padding:0;box-sizing:border-box}
html,body{width:1200px;height:2711px;overflow:hidden}
body{font-family:"Arimo",Arial,sans-serif;color:var(--ink);background:var(--white);position:relative}
.section{position:absolute;left:0;width:1200px}
.center{text-align:center}
.title{font-size:28px;font-weight:700;text-transform:uppercase;letter-spacing:.3px}
.title em{font-style:normal;color:var(--green)}
.lead{font-size:12px;line-height:22px;width:660px;margin:0 auto}

/* nav */
.topbar{top:0;height:90px;border-top:4px solid var(--green);background:var(--white)}
.brand{position:absolute;left:87px;top:30px;display:flex;align-items:center;gap:10px;font-size:22px;font-weight:700;color:var(--ink)}
.brand-mark{width:16px;height:16px;background:var(--green);border-radius:50%}
.nav{position:absolute;right:86px;top:38px;display:flex;gap:48px;list-style:none;font-size:12px;font-weight:700}
.nav li{color:var(--ink)}
.nav li.active{color:var(--green)}

/* hero */
.hero{top:90px;height:550px;overflow:hidden}
.hero-photo{position:absolute;inset:0;background:linear-gradient(100deg,#6f8a55 0%,#8ea57a 30%,#b8c6cf 55%,#9fb0bf 100%)}
.hero-cut{position:absolute;left:0;top:0}
.hero-copy{position:absolute;left:86px;top:182px;color:var(--white)}
.hero-copy h1{font-size:38px;font-weight:700;letter-spacing:.5px}
.hero-copy p{font-size:23px;line-height:34px;margin-top:10px}
.dots{position:absolute;left:556px;top:486px;display:flex;gap:4px}
.dots span{width:12px;height:12px;border:1.5px solid var(--white);border-radius:50%}
.dots span.on{background:var(--white)}

/* how */
.how{top:640px;height:570px;background:var(--light)}
.how .title{padding-top:44px}
.video{position:absolute;left:200px;top:110px;width:802px;height:400px;background:linear-gradient(180deg,#5d86c4 0%,#a9c2e3 45%,#3c4b5e 70%,#23303e 100%)}
.video-bar{position:absolute;left:0;bottom:0;width:100%;height:28px;background:var(--player);border-top:4px solid #9a9a9a}
.play{position:absolute;left:367px;top:152px;width:68px;height:68px;border:2px solid var(--white);border-radius:50%;background:rgba(0,0,0,.25);display:flex;align-items:center;justify-content:center}
.play::after{content:"";margin-left:6px;border-left:20px solid #fff;border-top:12px solid transparent;border-bottom:12px solid transparent}

/* contact strip */
.strip{top:1210px;height:96px;background:var(--green);color:var(--white)}
.strip-item{position:absolute;top:24px;display:flex;align-items:center;gap:20px;font-size:22px;font-weight:700;white-space:nowrap}
.ring{width:48px;height:48px;border:2px solid var(--white);border-radius:50%;display:flex;align-items:center;justify-content:center;flex:none}

/* work */
.work{top:1306px;height:431px;background:var(--dark);color:var(--white)}
.work .title{padding-top:36px}
.work .lead{color:#ddd;margin-top:12px}
.thumb{position:absolute;top:161px;width:332px;height:230px}
.thumb .ring{position:absolute;left:135px;top:84px;width:62px;height:62px}
.thumb .ring::after{content:"";margin-left:5px;border-left:16px solid #fff;border-top:10px solid transparent;border-bottom:10px solid transparent}
.arrow{position:absolute;top:218px}

/* why */
.why{top:1737px;height:475px;background:var(--light)}
.why .title{padding-top:44px}
.why .lead{color:var(--muted);margin-top:14px}
.feature{position:absolute;width:480px}
.feature .badge{position:absolute;left:0;top:0;width:94px;height:94px;border-radius:50%;border:3px solid var(--green);padding:4px;background:var(--white)}
.feature .badge div{width:100%;height:100%;border-radius:50%;background:var(--green);display:flex;align-items:center;justify-content:center}
.feature h3{position:absolute;left:124px;top:10px;font-size:13px;font-weight:700;text-transform:uppercase}
.feature p{position:absolute;left:124px;top:36px;width:370px;font-size:11px;line-height:21px;color:var(--muted)}

/* contact */
.contact{top:2212px;height:428px;background:var(--darker);color:var(--white)}
.contact .title{padding-top:26px}
.contact .lead{color:#ccc;margin-top:10px}
.field{position:absolute;background:var(--white);border-radius:4px;font-size:11px;color:#666;padding:14px 18px}
.send{position:absolute;left:477px;top:328px;width:245px;height:42px;background:linear-gradient(var(--green),var(--green-dark));border-radius:3px;color:var(--white);font-weight:700;font-size:14px;display:flex;align-items:center;justify-content:center}

/* footer */
.footer{top:2640px;height:71px;background:var(--green);color:var(--white)}
.copy{position:absolute;left:86px;top:29px;font-size:11px}
.foot-call{position:absolute;left:352px;top:24px;display:flex;align-items:center;gap:10px;font-size:18px;font-weight:700}
.foot-brand{position:absolute;right:86px;top:24px;font-size:18px;font-weight:700}
</style>
</head>
<body>

<header class="section topbar">
  <div class="brand"><span class="brand-mark"></span>SkyNestClips</div>
  <ul class="nav">
    <li class="active">HOME</li><li>OUR SERVICES</li><li>ABOUT US</li><li>PORTFOLIO</li><li>CONTACT US</li>
  </ul>
</header>

<section class="section hero">
  <div class="hero-photo" role="img" aria-label="Aerial camera drone flying in front of a leafy house garden"></div>
  <svg class="hero-cut" width="1200" height="550" viewBox="0 0 1200 550"><polygon points="0,452 600,550 1200,452 1200,550 0,550" fill="#f3f4f6"/></svg>
  <div class="hero-copy">
    <h1>SKYNESTCLIPS</h1>
    <p>We Film Your Home To Increase Your<br>Chances of Sale</p>
  </div>
  <div class="dots"><span></span><span></span><span class="on"></span><span></span><span></span></div>
</section>

<section class="section how">
  <h2 class="title center">How does <em>it works?</em></h2>
  <div class="video" role="img" aria-label="Explainer video still: drone remote with tablet over a city waterfront">
    <div class="play"></div>
    <div class="video-bar"></div>
  </div>
</section>

<section class="section strip">
  <div class="strip-item" style="left:160px">
    <span class="ring"><svg width="20" height="20" viewBox="0 0 24 24"><path d="M6.6 10.8a15 15 0 0 0 6.6 6.6l2.2-2.2a1 1 0 0 1 1-.25 11.4 11.4 0 0 0 3.6.57 1 1 0 0 1 1 1V20a1 1 0 0 1-1 1A17 17 0 0 1 3 4a1 1 0 0 1 1-1h3.5a1 1 0 0 1 1 1c0 1.25.2 2.45.57 3.57a1 1 0 0 1-.25 1z" fill="#fff"/></svg></span>
    CALL US : 31620487315
  </div>
  <div class="strip-item" style="left:570px">
    <span class="ring"><svg width="20" height="16" viewBox="0 0 20 16"><rect x="1" y="1" width="18" height="14" fill="none" stroke="#fff" stroke-width="2"/><path d="M1 1l9 7 9-7" fill="none" stroke="#fff" stroke-width="2"/></svg></span>
    EMAIL : contact@skynestclips.example
  </div>
</section>

<section class="section work">
  <h2 class="title center">Our Work</h2>
  <p class="lead center">Sed ut perspiciatis unde omnis iste natus error sit voluptatem accusantium doloremque laudantium, totam rem aperiam, ab illo inventore veritatis et quasi architecto beatae vitae dicta sunt explicabo.</p>
  <svg class="arrow" style="left:38px" width="14" height="120" viewBox="0 0 14 120"><path d="M13 0L1 60l12 60" fill="none" stroke="#aaa" stroke-width="1.5"/></svg>
  <div class="thumb" style="left:86px;background:linear-gradient(#c9d3de,#8f8f8f)" role="img" aria-label="Portfolio clip: drone hovering over a city street"><span class="ring"></span></div>
  <div class="thumb" style="left:435px;background:linear-gradient(#3f6fb5,#8aa0b5 60%,#4c5d6e)" role="img" aria-label="Portfolio clip: drone above a harbour at dusk"><span class="ring"></span></div>
  <div class="thumb" style="left:782px;background:linear-gradient(120deg,#58723b,#8ea462 55%,#7f97b8)" role="img" aria-label="Portfolio clip: drone over a green garden"><span class="ring"></span></div>
  <svg class="arrow" style="left:1148px" width="14" height="120" viewBox="0 0 14 120"><path d="M1 0l12 60L1 120" fill="none" stroke="#aaa" stroke-width="1.5"/></svg>
</section>

<section class="section why">
  <h2 class="title center">Why <em>us?</em></h2>
  <p class="lead center">Sed ut perspiciatis unde omnis iste natus error sit voluptatem accusantium doloremque laudantium, totam rem aperiam, ab illo inventore veritatis et quasi architecto beatae vitae dicta sunt explicabo.</p>

  <div class="feature" style="left:87px;top:155px">
    <div class="badge"><div><svg width="40" height="40" viewBox="0 0 40 40"><circle cx="20" cy="20" r="14" fill="none" stroke="#fff" stroke-width="3"/><text x="20" y="27" font-size="18" font-weight="700" fill="#fff" text-anchor="middle" font-family="Arial">$</text></svg></div></div>
    <h3>Cheap</h3>
    <p>Sed ut perspiciatis unde omnis iste natus error sit voluptatem accus antium doloremque laudantium, totam rem aperiam, ab illo inventore architecto beatae vitae dicta sunt explicabo.</p>
  </div>
  <div class="feature" style="left:627px;top:155px">
    <div class="badge"><div><svg width="40" height="40" viewBox="0 0 40 40" fill="none" stroke="#fff" stroke-width="3"><path d="M6 12h8l12 16h8M6 28h8l12-16h8"/><path d="M30 8l4 4-4 4M30 24l4 4-4 4"/></svg></div></div>
    <h3>Flexible</h3>
    <p>Sed ut perspiciatis unde omnis iste natus error sit voluptatem accus antium doloremque laudantium, totam rem aperiam, ab illo inventore architecto beatae vitae dicta sunt explicabo.</p>
  </div>
  <div class="feature" style="left:87px;top:311px">
    <div class="badge"><div><svg width="40" height="40" viewBox="0 0 40 40" fill="none" stroke="#fff" stroke-width="3"><circle cx="20" cy="16" r="10"/><path d="M15 16l4 4 6-7M13 25l-4 10 6-2 3 5 2-8M27 25l4 10-6-2-3 5-2-8"/></svg></div></div>
    <h3>9K Quality</h3>
    <p>Sed ut perspiciatis unde omnis iste natus error sit voluptatem accus antium doloremque laudantium, totam rem aperiam, ab illo inventore architecto beatae vitae dicta sunt explicabo.</p>
  </div>
  <div class="feature" style="left:627px;top:311px">
    <div class="badge"><div><svg width="40" height="40" viewBox="0 0 40 40" fill="#fff"><rect x="6" y="26" width="5" height="8"/><rect x="14" y="22" width="5" height="12"/><rect x="22" y="18" width="5" height="16"/><rect x="30" y="12" width="5" height="22"/><path d="M6 20L18 10l6 5 9-9" fill="none" stroke="#fff" stroke-width="3"/></svg></div></div>
    <h3>Increase Sale Chance</h3>
    <p>Sed ut perspiciatis unde omnis iste natus error sit voluptatem accus antium doloremque laudantium, totam rem aperiam, ab illo inventore architecto beatae vitae dicta sunt explicabo.</p>
  </div>
</section>

<section class="section contact">
  <h2 class="title center">Contact Us</h2>
  <p class="lead center">Sed ut perspiciatis unde omnis iste natus error sit voluptatem accusantium doloremque laudantium, totam rem aperiam, ab illo inventore veritatis et quasi architecto beatae vitae dicta sunt explicabo.</p>
  <div class="field" style="left:345px;top:141px;width:251px;height:43px">First Name :</div>
  <div class="field" style="left:604px;top:141px;width:251px;height:43px">Last Name :</div>
  <div class="field" style="left:345px;top:192px;width:251px;height:43px">Phone :</div>
  <div class="field" style="left:604px;top:192px;width:251px;height:43px">Email :</div>
  <div class="field" style="left:345px;top:242px;width:510px;height:68px">Message :</div>
  <div class="send">SEND</div>
</section>

<footer class="section footer">
  <p class="copy">© 2016 SkyNestClips All rights reserved.</p>
  <div class="foot-call"><svg width="16" height="16" viewBox="0 0 24 24"><path d="M6.6 10.8a15 15 0 0 0 6.6 6.6l2.2-2.2a1 1 0 0 1 1-.25 11.4 11.4 0 0 0 3.6.57 1 1 0 0 1 1 1V20a1 1 0 0 1-1 1A17 17 0 0 1 3 4a1 1 0 0 1 1-1h3.5a1 1 0 0 1 1 1c0 1.25.2 2.45.57 3.57a1 1 0 0 1-.25 1z" fill="#fff"/></svg>CALL US : 31620487315</div>
  <div class="foot-brand">SkyNestClips</div>
</footer>

</body>
</html>
```